Leuchtkasten für Pflegedienst
Zielgruppe
Wir sind ein ambulnter Pflegedienst in Rostock. Derzeit befindet sich am Haus ein runder Leuchtkasten mit dem alten Logo. Das Logo wurde erneuert. Nun soll der Leuchtkasten mit einem Durchmessr von 80 cm neu gestaltet werden.
Aufgabenstellung
bitte zwei unterscheideliche Entwürfe für die Vorder und die Rückseite. Es sollte auf der einen Seite vielleicht das Logo anthalten sein und auf der anderen Seite eine andere kreative Idee. Hauskrankenpflege Sorgenhaus Linde sollten enthalten sein, sowie die Telefonummer 0381-52946138
Auf der anderen Seite wurde ein Schriftzug in Edelstahl rostoptik montiert.
Wichtig ist, dass das der ENtwurf auf einer durchleichtbaren Folie gedruckt werden kann.
Der KAffee slogan war füe eine andere Aktion und sollte nicht auf den Leuchtkasten.

```html
<!DOCTYPE html>
<html lang="de">
<head>
<meta charset="utf-8">
<title>Leuchtkasten Sorgenhaus Linde – Vorder- und Rückseite</title>
<link rel="stylesheet" href="https://fonts.googleapis.com/css2?family=Fira+Sans:wght@600;700&display=swap">
<style>
  :root {
    --brand-blue: #2f7db8;
    --brand-navy: #161d33;
    --paper: #ffffff;
    --edge: #1a1a1a;
  }
  html, body {
    margin: 0;
    padding: 0;
    width: 1200px;
    height: 1106px;
    overflow: hidden;
    background: var(--paper);
  }
  .sheet {
    display: block;
    width: 1200px;
    height: 1106px;
  }
  .face-edge { fill: var(--paper); stroke: var(--edge); stroke-width: 1; }
  .band { fill: var(--brand-navy); }
  .emblem-ring { fill: none; stroke: var(--brand-blue); }
  .brand-name {
    font-family: "Fira Sans", sans-serif;
    font-weight: 700;
    text-anchor: middle;
  }
  .brand-name--front { fill: var(--brand-navy); font-size: 64px; }
  .brand-name--back { fill: var(--brand-blue); font-size: 40px; }
  .phone {
    font-family: "Fira Sans", sans-serif;
    font-weight: 700;
    font-size: 36px;
    fill: var(--paper);
  }
  .ring-text {
    font-family: "Fira Sans", sans-serif;
    font-weight: 600;
    font-size: 34px;
  }
  .ring-text--blue { fill: var(--brand-blue); }
  .ring-text--navy { fill: var(--brand-navy); }
</style>
</head>
<body>
<svg class="sheet" viewBox="0 0 1200 1106" xmlns="http://www.w3.org/2000/svg" aria-label="Leuchtkasten Vorder- und Rückseite">
  <defs>
    <clipPath id="front-face-clip">
      <circle cx="0" cy="0" r="280"/>
    </clipPath>
    <path id="ring-path" d="M -232 0 A 232 232 0 1 1 232 0 A 232 232 0 1 1 -232 0"/>
  </defs>

  <!-- Vorderseite: Name und Telefonnummer -->
  <g class="face face--front" transform="translate(300 553)">
    <circle class="face-edge" cx="0" cy="0" r="280"/>
    <g clip-path="url(#front-face-clip)">
      <path class="band" d="M -290 22 Q -70 190 215 192 L 300 192 L 300 300 L -300 300 Z"/>
    </g>
    <circle class="emblem-ring" cx="8" cy="-145" r="95" stroke-width="9"/>
    <text class="brand-name brand-name--front" x="0" y="28">Sorgenhaus</text>
    <text class="brand-name brand-name--front" x="0" y="100">Linde</text>
    <text class="phone" transform="translate(-190 158) rotate(20)" textLength="250" lengthAdjust="spacingAndGlyphs">0381-52946138</text>
  </g>

  <!-- Rückseite: umlaufender Schriftzug -->
  <g class="face face--back" transform="translate(900 553)">
    <circle class="face-edge" cx="0" cy="0" r="280"/>
    <circle class="emblem-ring" cx="0" cy="0" r="143" stroke-width="11"/>
    <text class="brand-name brand-name--back" x="0" y="-6">Sorgenhaus</text>
    <text class="brand-name brand-name--back" x="0" y="42">Linde</text>

    <text class="ring-text ring-text--blue"><textPath href="#ring-path" startOffset="40" textLength="300" lengthAdjust="spacingAndGlyphs">Hauskrankenpflege</textPath></text>
    <text class="ring-text ring-text--navy"><textPath href="#ring-path" startOffset="16">•</textPath></text>

    <text class="ring-text ring-text--navy"><textPath href="#ring-path" startOffset="404" textLength="300" lengthAdjust="spacingAndGlyphs">Hauskrankenpflege</textPath></text>
    <text class="ring-text ring-text--navy"><textPath href="#ring-path" startOffset="380">•</textPath></text>

    <text class="ring-text ring-text--blue"><textPath href="#ring-path" startOffset="768" textLength="300" lengthAdjust="spacingAndGlyphs">Hauskrankenpflege</textPath></text>
    <text class="ring-text ring-text--navy"><textPath href="#ring-path" startOffset="744">•</textPath></text>

    <text class="ring-text ring-text--navy"><textPath href="#ring-path" startOffset="1132" textLength="300" lengthAdjust="spacingAndGlyphs">Hauskrankenpflege</textPath></text>
    <text class="ring-text ring-text--navy"><textPath href="#ring-path" startOffset="1108">•</textPath></text>
  </g>
</svg>
</body>
</html>
```